Glass window Vinyl

We are in need of window vinyls for the building shown in the photos. The current vinyls will come down, and we will install the new signage created by this process. We need to advertise:

"Harwell's Landing Pop Up Market"

Then, below that, it should say for rental inquiries call : 555.613.0872 with our logo which is attached along with our colors and brand guidelines. You may add more color to the Harwells landing pop up market signage if appropriate. It should be large enough to be easily read from the road by those passing by.

```html
<!DOCTYPE html>
<html lang="en">
<head>
<meta charset="utf-8">
<title>Harwell's Landing Pop Up Market – Window Vinyl</title>
<link rel="stylesheet" href="https://fonts.googleapis.com/css2?family=Lato:wght@400;500&display=swap">
<style>
  :root {
    --backdrop: #4a4a4a;
    --teal: #23404d;
    --gold: #b7a170;
    --white: #ffffff;
    --siding-light: #d9dcdf;
    --siding-mid: #b9bdc2;
    --trim: #f3f3f1;
  }
  * { margin: 0; padding: 0; box-sizing: border-box; }
  html, body {
    width: 1200px;
    height: 1200px;
    overflow: hidden;
    background: var(--backdrop);
  }
  .vinyl {
    position: absolute;
    left: 133px;
    top: 133px;
    width: 934px;
    height: 933px;
    font-family: "Lato", sans-serif;
  }
  .header-band {
    position: absolute;
    left: 0; top: 0;
    width: 100%;
    height: 359px;
    background: var(--teal);
    text-align: center;
  }
  .brand {
    position: absolute;
    top: 52px;
    left: 0; width: 100%;
    display: flex;
    flex-direction: column;
    align-items: center;
    gap: 18px;
  }
  .brand-square {
    width: 22px;
    height: 22px;
    background: var(--gold);
  }
  .brand-name {
    color: var(--white);
    font-weight: 400;
    font-size: 27px;
    letter-spacing: 5px;
    text-transform: uppercase;
  }
  .event-title {
    position: absolute;
    top: 188px;
    left: 0; width: 100%;
    color: var(--gold);
    font-weight: 400;
    font-size: 64px;
    line-height: 72px;
    letter-spacing: -0.5px;
    text-transform: uppercase;
  }
  .gold-rule {
    position: absolute;
    left: 0; top: 359px;
    width: 100%;
    height: 5px;
    background: var(--gold);
  }
  .storefront-photo {
    position: absolute;
    left: 0; top: 364px;
    width: 100%;
    height: 303px;
    background: linear-gradient(180deg, var(--siding-light) 0%, var(--trim) 45%, var(--siding-mid) 100%);
  }
  .contact-band {
    position: absolute;
    left: 0; top: 667px;
    width: 100%;
    height: 266px;
    background: var(--gold);
    color: var(--teal);
  }
  .contact-label {
    position: absolute;
    left: 67px;
    top: 32px;
    width: 798px;
    font-size: 53px;
    font-weight: 400;
    line-height: 64px;
    letter-spacing: -0.3px;
    text-transform: uppercase;
    white-space: nowrap;
    padding-bottom: 6px;
    border-bottom: 3px solid var(--teal);
  }
  .contact-phone {
    position: absolute;
    left: 62px;
    top: 114px;
    font-size: 126px;
    font-weight: 400;
    line-height: 130px;
    letter-spacing: 1px;
    white-space: nowrap;
  }
</style>
</head>
<body>
  <main class="vinyl">
    <header class="header-band">
      <div class="brand">
        <span class="brand-square"></span>
        <span class="brand-name">Birchwood Row Properties</span>
      </div>
      <h1 class="event-title">Harwell's Landing<br>Pop Up Market</h1>
    </header>
    <div class="gold-rule"></div>
    <div class="storefront-photo" role="img" aria-label="Photo of the white-trimmed corner storefront with gray siding and rental posters in its windows"></div>
    <section class="contact-band">
      <p class="contact-label">For Rental Inquiries Call:</p>
      <p class="contact-phone">555.613.0872</p>
    </section>
  </main>
</body>
</html>
```